Supplement Company needs final product mockups and label design

We're a Supplement company launching 4 Hydration Supplement flavours. We need someone to re create the EXACT design with what ChatGPT has already generated and tweak the design slightly so that spelling is correct and callout icons are designed. We then also need someone to do the back of label design that includes space for the barcode, nutrition table, blurb etc. Bonus if you have experience with PLDWX compliance regulations and designing supplement labels.

We want the other 3 flavours (Lime, Mango & Watermelon) to match the design of the strawberry flavour including details like all the callout icons on the left side of the front, the word "electrolytes" in the dark coloured box, the words "hydration powder" just above the callout icons. Please re - design the callout icons to better suit the callout.

I've also attached an image of what the nutrition label should look like.

Please include the Following on the back of the label:
"Directions: Mix 1 Scoop with 400-500ml of water & Mix well before drinking. Do not exceed 2 servings per day.

Why live when you can QORVEL?
Your body wasn’t made to run on sugar, chemicals, and artificial junk — and your hydration shouldn’t either. At QORVEL Nutrition, we’ve created a clean, mineral-rich formula with Brannock Shore Salt and essential electrolytes to fuel you the right way. No toxins, no fillers — just real ingredients that work with your body, not against it.
Hydrate the way nature intended. Live clean. QORVEL.

AUSTRALIAN OWNED AND MADE

Store in a cool, dry place below 30°C. Reseal after use"

Product Formula & Ingredients:

* Sodium (Sea Salt, Brannock Shore Salt®, Himalayan Pink Salt): 1000 mg
* Potassium (from Potassium Chloride): 200 mg
* Magnesium (from Magnesium Glycinate): 60 mg
* Total Carbohydrates: 0 g
* Sugars: 0 g
* Calories: 1 kcal

Ingredients:
Sea Salt, Citric Acid, Brannock Shore Salt®, Himalayan Pink Salt, Potassium Chloride, Magnesium Glycinate, Natural Flavour (e.g. Mango), Stevia Leaf Extract.
Updates

I would like to give designers more time to closely replicate what I have included in the brief and make sure they can create something very beautifully

Industry/Entity Type

Supplements

Font styles to use
Other font styles liked:
• Montserrat

Requirements
Must have
• Back of label design aswell and Australian Nutrition table
Nice to have
• Design as close to the Provided images as possible
Should not have
• Should not be too different to the attached images

```html
<!DOCTYPE html>
<html lang="en">
<head>
<meta charset="utf-8">
<title>QORVEL Nutrition – Strawberry Electrolytes Label</title>
<link href="https://fonts.googleapis.com/css2?family=Montserrat:wght@400;500;600;700;800&family=Oswald:wght@500;600;700&display=swap" rel="stylesheet">
<style>
  :root {
    --label-red: #d9262b;
    --label-red-deep: #a9141b;
    --label-dark: #2a1214;
    --ink-white: #ffffff;
    --panel-white: #ffffff;
    --panel-ink: #111111;
    --accent-dark: #3a0b0e;
    --page-bg: #ffffff;
  }
  * { box-sizing: border-box; margin: 0; padding: 0; }
  html, body {
    width: 1200px; height: 3200px; overflow: hidden;
    background: var(--page-bg);
    font-family: "Montserrat", sans-serif;
  }
  .label {
    position: absolute; left: 123px; top: 1407px;
    width: 955px; height: 383px;
    background: linear-gradient(120deg, var(--label-red) 0%, #cf1f25 50%, var(--label-red) 100%);
    box-shadow: 0 6px 14px rgba(0,0,0,0.25);
    overflow: hidden; color: var(--ink-white);
  }
  .back-copy {
    position: absolute; left: 24px; top: 56px; width: 256px;
    font-size: 9.2px; line-height: 1.6; font-weight: 500; text-align: justify;
    letter-spacing: -0.1px;
  }
  .back-copy p { margin-bottom: 0; }
  .brand-inline { font-weight: 800; font-style: italic; color: var(--accent-dark); }
  .lead { color: var(--accent-dark); font-weight: 700; }
  .storage { text-align: center; margin-top: 4px; }

  .front {
    position: absolute; left: 300px; top: 0; width: 356px; height: 383px;
    text-align: center;
  }
  .brand-name {
    position: absolute; left: 0; right: 0; top: 18px;
    font-weight: 800; font-size: 42px; line-height: 1; letter-spacing: 1px;
  }
  .brand-sub {
    position: absolute; left: 0; right: 0; top: 59px;
    font-weight: 600; font-size: 13px; letter-spacing: 3px; line-height: 1;
  }
  .flavour {
    position: absolute; left: 0; right: 0; top: 76px;
    font-family: "Oswald", sans-serif; font-weight: 700; font-size: 46px; line-height: 1;
    letter-spacing: 0.5px;
  }
  .product-box {
    position: absolute; left: 47px; top: 130px; width: 260px; height: 34px;
    background: var(--label-dark); border-radius: 9px;
    font-weight: 700; font-size: 26px; line-height: 34px; letter-spacing: 1px;
  }
  .format {
    position: absolute; left: 0; right: 0; top: 172px;
    font-weight: 600; font-size: 16px; letter-spacing: 0.5px;
  }
  .callouts { position: absolute; left: 61px; top: 198px; list-style: none; text-align: left; }
  .callouts li { display: flex; align-items: center; height: 35px; }
  .callouts svg { width: 24px; height: 24px; flex: none; }
  .callouts span { margin-left: 6px; font-size: 10.5px; line-height: 1.05; font-weight: 500; }
  .fruit-art {
    position: absolute; left: 111px; top: 195px; width: 162px; height: 137px;
    background: radial-gradient(ellipse at 45% 55%, #e43a33 0%, #b81a20 60%, rgba(169,20,27,0) 75%);
    border-radius: 50%;
  }
  .net-weight {
    position: absolute; left: 0; right: 0; top: 343px;
    font-family: "Oswald", sans-serif; font-weight: 600; font-size: 19px; line-height: 1.2;
  }

  .nutrition-panel {
    position: absolute; left: 678px; top: 56px; width: 195px; height: 207px;
    background: var(--panel-white); color: var(--panel-ink);
    padding: 6px 9px; font-size: 7px; line-height: 1.25;
  }
  .nutrition-panel h3 { font-size: 11px; font-weight: 700; text-align: center; margin-bottom: 4px; }
  .np-meta { font-size: 7.5px; border-bottom: 2px solid var(--panel-ink); padding-bottom: 3px; }
  .np-table { width: 100%; border-collapse: collapse; margin-top: 2px; }
  .np-table th { font-weight: 500; font-size: 6.5px; border-bottom: 1px solid var(--panel-ink); padding: 1px 0 2px; }
  .np-table td { padding: 2.5px 0; font-size: 7px; }
  .np-table td + td, .np-table th + th { text-align: center; }
  .np-table tr.sub td { padding-top: 1px; }

  .badge-space {
    position: absolute; left: 886px; top: 66px; width: 36px; height: 36px;
    border: 1.5px solid var(--ink-white); border-radius: 50%;
  }

  .ingredients {
    position: absolute; left: 678px; top: 269px; width: 255px;
    font-size: 9.2px; line-height: 1.6; font-weight: 500; text-align: justify;
    letter-spacing: -0.1px;
  }
</style>
</head>
<body>
  <section class="label" aria-label="Strawberry electrolytes wrap-around label">
    <div class="back-copy">
      <p>Why live when you can <span class="brand-inline">QORVEL?</span> Your body wasn't made to run on sugar, chemicals, and artificial junk, and your hydration shouldn't either. At <span class="brand-inline">QORVEL</span> Nutrition, we've created a clean, mineral-rich formula with Brannock Shore Salt and essential electrolytes to fuel you the right way. No toxins, no fillers, just real ingredients that work with your body, not against it. Hydrate the way nature intended. Live clean. <span class="brand-inline">QORVEL.</span></p>
      <p><span class="lead">Directions:</span> Mix 1 Scoop with 400-500ml of water &amp; Mix well before drinking. Do not exceed 2 servings per day.</p>
      <p>Manufactured by: <span class="brand-inline">QORVEL</span> Nutrition, 45 Harbour Lane, Sydney, Australia. Contact: info@qorvel.com | +61 200 555 014 Made in Australia | Batch No: 12345 | Best Before: 28/04/2026</p>
      <p class="storage">Store in a cool, dry place below 30°C.<br>Reseal after use</p>
    </div>

    <div class="front">
      <div class="brand-name">QORVEL</div>
      <div class="brand-sub">NUTRITION</div>
      <div class="flavour">STRAWBERRY</div>
      <div class="product-box">ELECTROLYTES</div>
      <div class="format">HYDRATION POWDER</div>
      <div class="fruit-art" role="img" aria-label="Photograph of a fresh strawberry on a red swirl"></div>
      <ul class="callouts">
        <li>
          <svg viewBox="0 0 24 24"><circle cx="12" cy="12" r="11" fill="#2a1214" stroke="#fff" stroke-width="1.2"/><ellipse cx="12" cy="13" rx="4.5" ry="6" fill="none" stroke="#fff" stroke-width="1.4"/><circle cx="12" cy="14.5" r="2" fill="#fff"/></svg>
          <span>KETO<br>FRIENDLY</span>
        </li>
        <li>
          <svg viewBox="0 0 24 24"><circle cx="12" cy="12" r="11" fill="#2a1214" stroke="#fff" stroke-width="1.2"/><rect x="8" y="8" width="8" height="8" fill="none" stroke="#fff" stroke-width="1.4"/><line x1="5" y1="19" x2="19" y2="5" stroke="#fff" stroke-width="1.6"/></svg>
          <span>SUGAR<br>FREE</span>
        </li>
        <li>
          <svg viewBox="0 0 24 24"><circle cx="12" cy="12" r="11" fill="#2a1214" stroke="#fff" stroke-width="1.2"/><path d="M7 17 C7 10 11 7 17 7 C17 13 14 17 7 17 Z" fill="none" stroke="#fff" stroke-width="1.4"/><line x1="7" y1="17" x2="14" y2="10" stroke="#fff" stroke-width="1.2"/></svg>
          <span>PALEO<br>FRIENDLY</span>
        </li>
        <li>
          <svg viewBox="0 0 24 24"><circle cx="12" cy="12" r="11" fill="#2a1214" stroke="#fff" stroke-width="1.2"/><line x1="12" y1="6" x2="12" y2="18" stroke="#fff" stroke-width="1.4"/><ellipse cx="9.5" cy="10" rx="1.6" ry="2.4" fill="#fff"/><ellipse cx="14.5" cy="10" rx="1.6" ry="2.4" fill="#fff"/><ellipse cx="9.5" cy="14" rx="1.6" ry="2.4" fill="#fff"/><ellipse cx="14.5" cy="14" rx="1.6" ry="2.4" fill="#fff"/><line x1="5" y1="19" x2="19" y2="5" stroke="#fff" stroke-width="1.4"/></svg>
          <span>GLUTEN<br>FREE</span>
        </li>
      </ul>
      <div class="net-weight">NET WT. 180g</div>
    </div>

    <div class="nutrition-panel">
      <h3>Nutrition Information</h3>
      <div class="np-meta">Servings per package: 1.00<br>Serving size: 350.00 g</div>
      <table class="np-table">
        <thead><tr><th></th><th>Average per<br>Serving</th><th>Average per<br>100 g</th></tr></thead>
        <tbody>
          <tr><td>Energy</td><td>4 kJ</td><td>40 kJ</td></tr>
          <tr><td>Protein</td><td>0.0 g</td><td>0.0 g</td></tr>
          <tr class="sub"><td>Fat, total<br>- saturated</td><td>0.0 g</td><td>0.0 g</td></tr>
          <tr class="sub"><td>Carbohydrate<br>- sugars</td><td>0.0 g</td><td>0.0 g</td></tr>
          <tr><td>Sodium</td><td>1000 mg</td><td>10000 mg</td></tr>
          <tr><td>Potassium</td><td>200 mg</td><td>2000 mg</td></tr>
          <tr><td>Magnesium</td><td>60 mg</td><td>600 mg</td></tr>
        </tbody>
      </table>
    </div>

    <div class="badge-space" role="img" aria-label="Space for origin badge"></div>

    <p class="ingredients"><span class="lead">Ingredients:</span> Sea Salt, Citric Acid, Brannock Shore Salt®, Himalayan Pink Salt, Potassium Chloride, Magnesium Glycinate, Natural Flavour (e.g. Mango), Stevia Leaf Extract.</p>
  </section>
</body>
</html>
```